Postcard Design

We provide humorous speechwriting and presentation coaching services, primarily for the wedding market (best man, father of the bride, maid of honor). We'd like a design that incoporates the blue and white logo colors into a nice overall design, with the pitch:
"Use the power of humor to deliver the BEST speech of your life!"
Target Market(s)
Wedding market (best man, bride/groom)
Industry/Entity Type
Wedding
Requirements
Must have
- Bulletpoints for services provided:
- Speechwriting
- Presentation Coaching
- Emcee & Officiant Services
Listing of benefits provided:
- Conquer stage fright
- Deliver your speech like a pro
- Be funny AND tactful
- Leave them wanting more
Contact info -
Derek Hanslow
Derek@JollyQuill.com
www.JollyQuill.com
Testimonial quotes:
"People are STILL raving about that speech at our wedding. Thanks Jolly Quill!"
- Karen & Paul Dessaro, Baltimore, MD
"With the help of Jolly Quill, my best man speech brought down the house!"
- Trent Galloway, Melville, NY

```html
<!DOCTYPE html>
<html lang="en">
<head>
<meta charset="utf-8">
<title>Jolly Quill Postcard</title>
<link href="https://fonts.googleapis.com/css2?family=Oswald:wght@500;700&family=Roboto:wght@400&display=swap" rel="stylesheet">
<style>
  :root {
    --navy: #1b2566;
    --navy-deep: #0f1650;
    --blue: #2e4aa8;
    --sky: #3d63c9;
    --white: #ffffff;
    --mist: #e9ebf2;
    --slate: #7d86a6;
    --ink: #2b2f3c;
  }
  * { margin: 0; padding: 0; box-sizing: border-box; }
  html, body { width: 1200px; height: 930px; overflow: hidden; background: var(--white); }
  .postcard {
    position: relative;
    width: 1200px;
    height: 930px;
    overflow: hidden;
    background: var(--mist);
  }
  .crowd-photo {
    position: absolute;
    inset: 0;
    background:
      radial-gradient(ellipse at 80% 30%, #4a66c8 0%, rgba(60,80,170,0.6) 20%, rgba(20,25,60,0) 45%),
      radial-gradient(ellipse at 95% 70%, #c9b3a6 0%, rgba(150,130,130,0) 35%),
      linear-gradient(100deg, #d7d9e2 0%, #9da3b8 35%, #2a2f4a 60%, #1c2034 100%);
  }
  .fade-left {
    position: absolute;
    inset: 0;
    background: linear-gradient(90deg, rgba(255,255,255,0.92) 0%, rgba(255,255,255,0.7) 30%, rgba(255,255,255,0) 52%);
  }
  .fade-bottom {
    position: absolute;
    left: 0; right: 0; bottom: 0;
    height: 430px;
    background: linear-gradient(180deg, rgba(255,255,255,0) 0%, rgba(245,246,250,0.85) 45%, rgba(240,241,246,0.95) 100%);
  }
  .chevrons { position: absolute; inset: 0; }
  .brand-seal {
    position: absolute;
    left: 128px; top: 3px;
    width: 254px; height: 254px;
    border-radius: 50%;
    background: var(--navy);
    border: 6px solid var(--white);
    box-shadow: 0 0 0 3px var(--navy);
    display: flex;
    align-items: center;
    justify-content: center;
    text-align: center;
  }
  .brand-name {
    font-family: "Oswald", sans-serif;
    font-weight: 700;
    font-size: 44px;
    line-height: 1.05;
    letter-spacing: 1px;
    color: var(--white);
    text-transform: uppercase;
  }
  .pitch {
    position: absolute;
    left: 30px; top: 318px;
    font-family: "Oswald", sans-serif;
    font-weight: 700;
    font-size: 55px;
    line-height: 52px;
    color: var(--navy);
    text-transform: uppercase;
    letter-spacing: 0.5px;
  }
  .services-label {
    position: absolute;
    left: 0; top: 518px;
    width: 356px; height: 62px;
    background: linear-gradient(90deg, var(--navy-deep) 0%, var(--blue) 100%);
    clip-path: polygon(0 0, 100% 0, 92% 100%, 0 100%);
    font-family: "Oswald", sans-serif;
    font-weight: 500;
    font-size: 40px;
    line-height: 62px;
    color: var(--white);
    padding-left: 42px;
    text-transform: uppercase;
  }
  .service-list {
    position: absolute;
    left: 57px; top: 600px;
    display: flex;
    gap: 23px;
    list-style: none;
  }
  .service-card {
    width: 345px;
    height: 276px;
    background: var(--white);
    padding: 3px 3px 0;
    box-shadow: 0 2px 6px rgba(0,0,0,0.15);
  }
  .service-card:last-child { margin-left: 6px; }
  .service-visual { width: 100%; height: 222px; }
  .visual-pen { background: linear-gradient(135deg, #efe6d2 0%, #c9b994 50%, #5a4a2e 100%); }
  .visual-stage { background: radial-gradient(ellipse at 50% 35%, #6f9ae8 0%, #1f49b8 55%, #0d2a7a 100%); }
  .visual-reception { background: linear-gradient(160deg, #b89a84 0%, #8a7062 40%, #e3d6cc 75%, #f3eee8 100%); }
  .service-name {
    font-family: "Roboto", sans-serif;
    font-weight: 400;
    font-size: 26px;
    line-height: 50px;
    text-align: center;
    color: var(--ink);
  }
</style>
</head>
<body>
  <main class="postcard">
    <div class="crowd-photo" role="img" aria-label="Audience with raised hands cheering a speaker on stage"></div>
    <div class="fade-left"></div>
    <div class="fade-bottom"></div>

    <svg class="chevrons" width="1200" height="930" viewBox="0 0 1200 930" aria-hidden="true">
      <polygon points="640,0 960,0 1200,240 1200,560" fill="rgba(255,255,255,0.28)"/>
      <polygon points="560,405 960,0 1010,0 620,405 1200,960 1130,960" fill="rgba(170,178,205,0.75)"/>
      <polygon points="600,405 985,0 1000,0 615,405 1200,955 1180,955" fill="rgba(255,255,255,0.85)"/>
      <polygon points="900,0 1200,0 1200,300" fill="rgba(255,255,255,0.18)"/>
    </svg>

    <div class="brand-seal">
      <span class="brand-name">Jolly<br>Quill</span>
    </div>

    <h1 class="pitch">Use the power of humor<br>to deliver the best<br>speech of your life</h1>

    <div class="services-label">Services:</div>

    <ul class="service-list">
      <li class="service-card">
        <div class="service-visual visual-pen" role="img" aria-label="Fountain pen resting on handwritten paper"></div>
        <p class="service-name">Speechwriting</p>
      </li>
      <li class="service-card">
        <div class="service-visual visual-stage" role="img" aria-label="Speaker silhouetted on a blue stage before an audience"></div>
        <p class="service-name">Presentation Coaching</p>
      </li>
      <li class="service-card">
        <div class="service-visual visual-reception" role="img" aria-label="Guests seated at a wedding reception table"></div>
        <p class="service-name">Emcee &amp; Officiant Services</p>
      </li>
    </ul>
  </main>
</body>
</html>
```